To Build a Wordpress Website/Blog Post

I want to build a wordpress website and blog platform for a personal
Transformation project that will also form part of a multi channel/platform offering inc Instagram, podcasts, Friendbook, YouTube all of which I am looking for help on. I will aim to blog c 1/2 times per week and would like to build an interactive offering that is future proof in terms
Of sizing and extension into another larger brand offering. (Can anyone pls tell me if/why I would Need a coded design? I’m afraid I don’t Know If I need this?). Tha is
Updates

Have now added ‘coded’ as an upgrade so worth allowing more time For designers

All. Just to let you know that I have added ‘coded’ as an upgrade as I want the Wordpress website to Be built as well as designed. Please see TomVale.com for the look and feel I want. I do not need the exommerce functionality at this time but if we could have each of those menu items built that would be great. The ones to show are Home, blog, podcast, gavins story, contact, resources plus maybe links to Instagram, Friendbook and YouTube? Many tha ks

Target Market(s)

Men ages 35-60. Corporate, professional crowd for sure but all males globally. Ex athletes, Dads, interested in health and well-being. Endurance athletes. Interested in men’s health inc mental health, burnout, stress, middle age, life switching, potentiality, direction.

Industry/Entity Type

Health And Wellness

Coding

Coded - Design and coding required

Number of Pages Required

5+ page

Font styles to use
Serif
Sans Serif

Colors
3277b5
33a6d7
0493ce
acd136
1b1b1b
b1b1b1
b2b2b2
dddddd

Requirements
Must have
• A professional but inspirational appearance. Wordpress platform. Needs to host blogs and podcasts and images and feedback/forums plus archives and linking into a multi channel/platform offering. I need to
• Own the ip, be able to post text and images from mobile. It must be responsive and inc my logos and be editable by me at any time/registered in my Name. I enjoy greyscale and muted shades but will highlight other colours below
Nice to have
• See tomvale for high production values. This will Appeal to professionals (mostly men) that are aged 35-60 and interested in transformation. The idea is to do 50 things by the time I am 50 (Nov 19). So will update and blog etc but also Link to podcasts and Instagram and fbook etc
Should not have
• Too many cliches. Poor design and low production values. Needs to be aspirational

```html
<!DOCTYPE html>
<html lang="en">
<head>
<meta charset="utf-8">
<title>Summit — Things to do before 50</title>
<link rel="stylesheet" href="https://fonts.googleapis.com/css2?family=Oswald:wght@400;500;600;700&family=Open+Sans:wght@400;600;700&display=swap">
<style>
  :root{
    --blue:#3277b5;
    --blue-light:#33a6d7;
    --ink:#1b1b1b;
    --text:#555555;
    --btn:#3a3a3a;
    --grey-band:#eeeeee;
    --grey-news:#a9a9a9;
    --footer:#3b3b3b;
    --line:#dddddd;
    --white:#ffffff;
  }
  *{margin:0;padding:0;box-sizing:border-box;}
  html,body{width:1200px;height:3284px;overflow:hidden;}
  body{font-family:"Open Sans",Arial,sans-serif;color:var(--text);background:var(--white);position:relative;}

  .btn{display:inline-block;background:var(--btn);color:var(--white);font-size:15px;font-weight:600;padding:12px 24px;border-radius:3px;text-decoration:none;}

  /* Hero */
  .hero{position:absolute;left:0;top:0;width:1200px;height:632px;overflow:hidden;}
  .hero-photo{position:absolute;inset:0;background:linear-gradient(100deg,#7a4f46 0%,#a3675a 22%,#6d8793 45%,#9fb3bd 62%,#b56a5d 82%,#6a4a48 100%);}
  .hero-shade{position:absolute;inset:0;background:linear-gradient(180deg,rgba(0,0,0,.45) 0%,rgba(0,0,0,.15) 40%,rgba(0,0,0,.35) 100%);}
  .site-header{position:absolute;left:0;top:0;width:1200px;height:110px;}
  .brand{position:absolute;left:120px;top:14px;display:flex;align-items:center;gap:12px;color:var(--white);font-family:"Oswald",sans-serif;font-size:34px;font-weight:600;letter-spacing:2px;}
  .brand-mark{width:22px;height:22px;border-radius:50%;background:var(--white);}
  .main-nav{position:absolute;right:96px;top:56px;display:flex;gap:34px;}
  .main-nav a{color:var(--white);text-decoration:none;font-size:16px;font-weight:600;}
  .hero-content{position:absolute;left:0;top:222px;width:1200px;text-align:center;color:var(--white);}
  .hero-title{font-family:"Oswald",sans-serif;font-weight:700;font-size:52px;letter-spacing:1px;text-transform:uppercase;}
  .hero-text{width:640px;margin:18px auto 0;font-size:15px;line-height:1.6;}
  .hero-content .btn{margin-top:46px;background:var(--white);color:var(--ink);}
  .slider-arrow{position:absolute;top:360px;}
  .slider-arrow.prev{left:36px;}
  .slider-arrow.next{right:36px;}

  /* Section titles */
  .section-title{font-family:"Oswald",sans-serif;font-weight:700;font-size:30px;color:var(--blue);text-transform:uppercase;text-align:center;}
  .section-title::after{content:"";display:block;width:70px;height:3px;background:var(--blue);margin:10px auto 0;}

  /* About */
  .about{position:absolute;left:0;top:632px;width:1200px;height:428px;text-align:center;padding-top:76px;}
  .about p{width:860px;margin:0 auto;font-size:14px;line-height:1.7;}
  .about p.lead{margin-top:36px;}
  .about p + p{margin-top:14px;}
  .about .btn{margin-top:30px;}

  /* Photo strip */
  .moments{position:absolute;left:0;top:1060px;width:1200px;height:380px;display:flex;}
  .moment{width:240px;height:380px;position:relative;}
  .moment .label{position:absolute;left:0;top:140px;width:240px;text-align:center;color:var(--white);}
  .moment .label strong{display:block;font-family:"Oswald",sans-serif;font-size:24px;font-weight:600;}
  .moment .label span{font-size:15px;}
  .m1{background:linear-gradient(160deg,#8b7a70,#4f463f);}
  .m2{background:linear-gradient(160deg,#b6a99a,#6d6158);}
  .m3{background:linear-gradient(160deg,#6f94b4,#3a5f80);}
  .m4{background:linear-gradient(160deg,#e0a468,#9a5a3a);}
  .m5{background:linear-gradient(160deg,#c9c3b4,#7f786a);}
  .moment::before{content:"";position:absolute;inset:0;background:rgba(20,40,70,.25);}

  /* Cards */
  .blog{position:absolute;left:0;top:1440px;width:1200px;height:660px;padding-top:80px;}
  .podcast{position:absolute;left:0;top:2100px;width:1200px;height:550px;padding-top:34px;background:var(--grey-band);}
  .card-row{display:flex;justify-content:center;gap:28px;margin-top:62px;}
  .card{width:306px;text-align:center;}
  .card-photo{width:306px;height:178px;}
  .card-title{font-family:"Oswald",sans-serif;font-weight:600;font-size:19px;color:var(--ink);margin-top:30px;}
  .card p{font-size:12px;line-height:1.6;margin:10px auto 0;width:260px;}
  .card .btn{margin-top:22px;font-size:13px;padding:10px 20px;}
  .b1{background:linear-gradient(150deg,#d8c9b6,#8d7a66);}
  .b2{background:linear-gradient(150deg,#3e4a5a,#7a6a5a);}
  .b3{background:linear-gradient(150deg,#b0a594,#5a544c);}
  .podcast .card-row{margin-top:46px;}
  .podcast .card-photo{height:166px;}
  .p1{background:linear-gradient(150deg,#9aa08c,#5c6350);}
  .p2{background:linear-gradient(150deg,#7f9a6a,#b9a98a);}
  .p3{background:linear-gradient(150deg,#8a8d94,#c46a3c);}
  .episode-tag{display:block;background:#555555;color:var(--white);font-size:13px;font-weight:600;padding:11px 0;width:240px;margin:10px auto 0;}
  .episode-tag.featured{background:var(--blue);}
  .podcast .card p{margin-top:22px;}

  /* Newsletter */
  .newsletter{position:absolute;left:0;top:2650px;width:1200px;height:275px;background:var(--grey-news);text-align:center;padding-top:44px;color:var(--white);}
  .newsletter h2{font-family:"Oswald",sans-serif;font-weight:600;font-size:30px;}
  .newsletter p{width:420px;margin:12px auto 0;font-size:13px;line-height:1.5;}
  .subscribe{display:flex;justify-content:center;margin-top:30px;}
  .subscribe .field{width:270px;height:36px;background:var(--white);color:#888;font-size:12px;text-align:left;padding:10px 14px;}
  .subscribe .submit{width:90px;height:36px;background:var(--blue);color:var(--white);font-size:12px;font-weight:700;padding-top:10px;}

  /* Footer */
  .site-footer{position:absolute;left:0;top:2925px;width:1200px;height:359px;background:var(--footer);color:#cfcfcf;}
  .footer-brand{position:absolute;left:110px;top:80px;display:flex;align-items:center;gap:16px;color:var(--white);font-family:"Oswald",sans-serif;font-size:46px;font-weight:600;letter-spacing:3px;}
  .footer-brand .brand-mark{width:40px;height:40px;}
  .footer-col{position:absolute;top:56px;}
  .footer-col h3{font-family:"Oswald",sans-serif;color:var(--white);font-size:16px;font-weight:600;margin-bottom:10px;}
  .footer-col li{list-style:none;font-size:12px;line-height:19px;}
  .col-links{left:464px;}
  .col-menu{left:724px;}
  .col-social{left:950px;}
  .social li{display:flex;align-items:center;gap:10px;margin-bottom:14px;}
  .social .dot{width:26px;height:26px;border-radius:50%;background:var(--blue);}
  .footer-rule{position:absolute;left:464px;top:268px;width:640px;height:1px;background:#5a5a5a;}
  .copyright{position:absolute;left:0;top:290px;width:1200px;text-align:center;font-size:12px;}
</style>
</head>
<body>

<section class="hero">
  <div class="hero-photo" role="img" aria-label="Group of friends walking along a busy city street at sunset"></div>
  <div class="hero-shade"></div>
  <header class="site-header">
    <div class="brand"><span class="brand-mark"></span>SUMMIT</div>
    <nav class="main-nav">
      <a href="#">Home</a><a href="#">Blog</a><a href="#">Gavin's Story</a><a href="#">Podcast</a><a href="#">Milestones</a><a href="#">Resources</a><a href="#">Contact</a>
    </nav>
  </header>
  <div class="hero-content">
    <h1 class="hero-title">Things to do before 50 age</h1>
    <p class="hero-text">Small steps every week add up to a bigger life. Fifty goals, one honest journey before the big birthday.</p>
    <a class="btn" href="#">Read More</a>
  </div>
  <svg class="slider-arrow prev" width="24" height="44" viewBox="0 0 24 44"><polyline points="20,4 4,22 20,40" fill="none" stroke="#fff" stroke-width="3"/></svg>
  <svg class="slider-arrow next" width="24" height="44" viewBox="0 0 24 44"><polyline points="4,4 20,22 4,40" fill="none" stroke="#fff" stroke-width="3"/></svg>
</section>

<section class="about">
  <h2 class="section-title">About Summit</h2>
  <p class="lead">Fifty things before fifty is a personal challenge about health, purpose and courage in midlife. Each month brings new goals, honest lessons and stories from men finding their next direction.</p>
  <p>Follow the journey through weekly blogs, candid podcasts and shared training plans. Join a community of fathers, athletes and professionals who believe the best years can still be ahead.</p>
  <a class="btn" href="#">Read More</a>
</section>

<section class="moments">
  <div class="moment m1" role="img" aria-label="Man with a road bike"><div class="label"><strong>LOREM IPSUM</strong><span>Sed ut perspiciatis</span></div></div>
  <div class="moment m2" role="img" aria-label="Man relaxing on a sofa"><div class="label"><strong>LOREM IPSUM</strong><span>Sed ut perspiciatis</span></div></div>
  <div class="moment m3" role="img" aria-label="Man sitting on a jetty by the sea"><div class="label"><strong>LOREM IPSUM</strong><span>Sed ut perspiciatis</span></div></div>
  <div class="moment m4" role="img" aria-label="Runner at sunset"><div class="label"><strong>LOREM IPSUM</strong><span>Sed ut perspiciatis</span></div></div>
  <div class="moment m5" role="img" aria-label="Man stretching outdoors"><div class="label"><strong>LOREM IPSUM</strong><span>Sed ut perspiciatis</span></div></div>
</section>

<section class="blog">
  <h2 class="section-title">Our Blog Posts</h2>
  <div class="card-row">
    <article class="card">
      <div class="card-photo b1" role="img" aria-label="Father and son at a table"></div>
      <h3 class="card-title">DUIS AUTE IRURE DOLOR</h3>
      <p>Duis aute irure dolor in reprehenderit in voluptate velit esse cillum dolore.</p>
      <a class="btn" href="#">Read More</a>
    </article>
    <article class="card">
      <div class="card-photo b2" role="img" aria-label="Man reading on a couch"></div>
      <h3 class="card-title">DUIS AUTE IRURE DOLOR</h3>
      <p>Duis aute irure dolor in reprehenderit in voluptate velit esse cillum dolore.</p>
      <a class="btn" href="#">Read More</a>
    </article>
    <article class="card">
      <div class="card-photo b3" role="img" aria-label="Man doing push-ups"></div>
      <h3 class="card-title">DUIS AUTE IRURE DOLOR</h3>
      <p>Duis aute irure dolor in reprehenderit in voluptate velit esse cillum dolore.</p>
      <a class="btn" href="#">Read More</a>
    </article>
  </div>
</section>

<section class="podcast">
  <h2 class="section-title">Our Podcast</h2>
  <div class="card-row">
    <article class="card">
      <div class="card-photo p1" role="img" aria-label="Podcast guest working outdoors"></div>
      <span class="episode-tag">Podcast Marcus Hale Ford</span>
      <p>Duis aute irure dolor in reprehenderit in voluptate velit esse cillum dolore.</p>
      <a class="btn" href="#">Listen Now</a>
    </article>
    <article class="card">
      <div class="card-photo p2" role="img" aria-label="Podcast guest in a garden"></div>
      <span class="episode-tag featured">Podcast Daniel Ortiz</span>
      <p>Duis aute irure dolor in reprehenderit in voluptate velit esse cillum dolore.</p>
      <a class="btn" href="#">Listen Now</a>
    </article>
    <article class="card">
      <div class="card-photo p3" role="img" aria-label="Podcast guest with family"></div>
      <span class="episode-tag">Podcast Superstar Simon Reyes</span>
      <p>Duis aute irure dolor in reprehenderit in voluptate velit esse cillum dolore.</p>
      <a class="btn" href="#">Listen Now</a>
    </article>
  </div>
</section>

<section class="newsletter">
  <h2>NEWSLETTER SUBSCRIBE</h2>
  <p>Get fresh stories, podcast episodes and training notes delivered to your inbox every week. No spam, just honest progress.</p>
  <div class="subscribe"><div class="field">Enter email address</div><div class="submit">SUBMIT</div></div>
</section>

<footer class="site-footer">
  <div class="footer-brand"><span class="brand-mark"></span>SUMMIT</div>
  <div class="footer-col col-links">
    <h3>LINKS</h3>
    <ul><li>TERMS &amp; CONDITIONS</li><li>PRIVACY POLICY</li><li>FAQ</li><li>PRESS</li></ul>
  </div>
  <div class="footer-col col-menu">
    <h3>MENU</h3>
    <ul><li>HOME</li><li>BLOG</li><li>GAVIN'S STORY</li><li>PODCAST</li><li>MILESTONES</li><li>RESOURCES</li><li>CONTACT</li></ul>
  </div>
  <div class="footer-col col-social">
    <h3>CONNECT WITH US</h3>
    <ul class="social"><li><span class="dot"></span>Friendbook</li><li><span class="dot"></span>Chirper</li><li><span class="dot"></span>Linkline</li></ul>
  </div>
  <div class="footer-rule"></div>
  <p class="copyright">Copyright @ 2018 Summit All Rights Reserved.</p>
</footer>

</body>
</html>
```